Wellness Coach/personal trainer Business Card Design Project

We need an eye catching logo design for a wellness coach / personal trainer who specializes in weight loss / body transformation / health coaching. We educate, empower, and support our clients on their weight loss journey. We want the look and feel described below on the business card design.

Target Market(s)

80 % women 20 % men
educated 30 - 50 women
vanity/appearance focused

Industry/Entity Type

Personal Trainer

Font styles to use
Serif

Colors
a54599
f9ed23
ffffff

Requirements
Must have
• name - Dorian Calvaske
phone - (888) 275 9146
web address - www.7PennyMover.example
tagline - Becasue Looking Good Matters
Nice to have
• see Look and Feel
Colorful, Playful, Elegant
Should not have
• no cartoons or animation

```html
<!DOCTYPE html>
<html lang="en">
<head>
<meta charset="utf-8">
<title>7Penny Mover – Business Card</title>
<link rel="stylesheet" href="https://fonts.googleapis.com/css2?family=Lora:ital,wght@0,400;0,500;0,600;1,400&display=swap">
<style>
  :root {
    --page-bg: #e9e6e1;
    --purple-light: #b857ab;
    --purple-dark: #8a3580;
    --card-white: #ffffff;
    --white-shade: #ececee;
    --yellow: #f9ed23;
    --yellow-soft: #fbf27a;
    --brand-purple: #a54599;
    --text-white: #ffffff;
  }
  * { margin: 0; padding: 0; box-sizing: border-box; }
  html, body { width: 1200px; height: 900px; overflow: hidden; }
  body {
    background: var(--page-bg);
    font-family: "Lora", serif;
    position: relative;
  }
  .business-card {
    position: absolute;
    left: 100px; top: 165px;
    width: 1000px; height: 570px;
    border-radius: 4px;
    overflow: hidden;
    box-shadow: 0 18px 40px rgba(0,0,0,.25);
  }
  .card-art { position: absolute; inset: 0; }
  .contact-panel {
    position: absolute;
    left: 70px; top: 58px;
    color: var(--text-white);
  }
  .holder-name {
    font-size: 32px; font-weight: 500; letter-spacing: 2px; line-height: 1;
  }
  .holder-role { font-size: 20px; margin-top: 10px; letter-spacing: .5px; }
  .address { font-size: 21px; line-height: 1.35; margin-top: 40px; letter-spacing: .5px; }
  .contact-list { list-style: none; margin-top: 36px; }
  .contact-list li {
    display: flex; align-items: center; gap: 14px;
    font-size: 19px; letter-spacing: .5px; height: 36px;
  }
  .contact-list li.small { font-size: 16px; }
  .contact-icon { width: 20px; height: 20px; flex: none; }
  .brand-lockup {
    position: absolute;
    left: 580px; top: 232px;
    display: flex; flex-direction: column; align-items: flex-start;
  }
  .brand-row { display: flex; align-items: center; gap: 16px; }
  .brand-dot {
    width: 52px; height: 52px; border-radius: 50%;
    background: var(--yellow);
  }
  .brand-name {
    font-size: 48px; font-weight: 600; color: var(--brand-purple);
    letter-spacing: .5px; line-height: 1;
  }
  .tagline {
    margin-top: 14px; margin-left: 68px;
    font-size: 19px; font-style: italic; color: var(--brand-purple);
    letter-spacing: .5px;
  }
</style>
</head>
<body>
  <section class="business-card">
    <svg class="card-art" viewBox="0 0 1000 570" width="1000" height="570" aria-hidden="true">
      <defs>
        <linearGradient id="purpleField" x1="0" y1="0" x2="1" y2="1">
          <stop offset="0" stop-color="var(--purple-light)"/>
          <stop offset="1" stop-color="var(--purple-dark)"/>
        </linearGradient>
        <radialGradient id="whiteField" cx=".75" cy=".4" r=".7">
          <stop offset="0" stop-color="var(--card-white)"/>
          <stop offset="1" stop-color="var(--white-shade)"/>
        </radialGradient>
        <linearGradient id="crescent" x1="0" y1="0" x2="0" y2="1">
          <stop offset="0" stop-color="var(--yellow)"/>
          <stop offset="1" stop-color="var(--yellow-soft)"/>
        </linearGradient>
      </defs>
      <rect class="purple-field" width="1000" height="570" fill="url(#purpleField)"/>
      <path class="white-field" d="M600 0 C440 70 370 280 440 570 L1000 570 L1000 0 Z" fill="url(#whiteField)"/>
      <path class="yellow-crescent" d="M640 12 C490 60 410 270 470 560 C440 300 490 120 640 12 Z" fill="url(#crescent)"/>
    </svg>

    <div class="contact-panel">
      <h1 class="holder-name">DORIAN CALVASKE</h1>
      <p class="holder-role">Managing Director</p>
      <p class="address">214 9th floor,Plaza<br>Ferncliff Road KLM</p>
      <ul class="contact-list">
        <li>
          <svg class="contact-icon" viewBox="0 0 20 20"><path d="M4 2 L8 2 L9 6 L7 8 C8 11 9 12 12 13 L14 11 L18 12 L18 16 C18 17 17 18 16 18 C8 17 3 12 2 4 C2 3 3 2 4 2 Z" fill="#fff"/></svg>
          (888) 275 9146
        </li>
        <li>
          <svg class="contact-icon" viewBox="0 0 20 20"><rect x="5" y="1" width="10" height="18" rx="2" fill="none" stroke="#fff" stroke-width="1.8"/><circle cx="10" cy="16" r="1" fill="#fff"/></svg>
          (888) 275 9146
        </li>
        <li>
          <svg class="contact-icon" viewBox="0 0 20 20"><rect x="2" y="8" width="16" height="10" rx="1" fill="#fff"/><rect x="5" y="2" width="10" height="7" fill="none" stroke="#fff" stroke-width="1.6"/></svg>
          (888) 275 9146
        </li>
        <li class="small">
          <svg class="contact-icon" viewBox="0 0 20 20"><rect x="1" y="4" width="18" height="12" fill="#fff"/><path d="M1 4 L10 11 L19 4" fill="none" stroke="#a54599" stroke-width="1.5"/></svg>
          hello@7pennymover.example
        </li>
        <li class="small">
          <svg class="contact-icon" viewBox="0 0 20 20"><circle cx="10" cy="10" r="8" fill="none" stroke="#fff" stroke-width="1.6"/><ellipse cx="10" cy="10" rx="3.5" ry="8" fill="none" stroke="#fff" stroke-width="1.3"/><path d="M2 10 H18" stroke="#fff" stroke-width="1.3"/></svg>
          www.7PennyMover.example
        </li>
      </ul>
    </div>

    <div class="brand-lockup">
      <div class="brand-row">
        <span class="brand-dot"></span>
        <span class="brand-name">7Penny Mover</span>
      </div>
      <p class="tagline">Becasue Looking Good Matters</p>
    </div>
  </section>
</body>
</html>
```